Kavak Verbatics web design: a translation company with corporate clients

Need a new website for my translation and localization company with file uploading capacity directed to email for quotation

old (very old) web site is www.kvkaktarim.example you can use the content text there or lorem ipsum, We will provide the texts. It will be in English - Turkish - French and German
For the content and overall layout: https://www.pellardlanguages.example/

For the color scheme you'll need to see logo's colors.

I am rebranding so new logo is uploaded The new adress will be www.kavakverbatics.example

Target Market(s)

Primarily corporate clients

Industry/Entity Type

It Company

Coding

Coded - Design and coding required

Number of Pages Required

5+ page

Font styles to use
Other font styles liked:
• Calibri

Requirements
Must have
• References on homepage (logos will be sent during design phase)
• Services: Translation, Interpretation, Localization&Consultancy, Translation API
• Quotation Form and file uploading
• Simple layout evoking reliability, speed and accuracy
Nice to have
• For the content and overall layout: https://www.pellardlanguages.example/
• Separate page for Translation Services: Marketing Translation, Legal Translation, Technical Translation, Personal Translation
• and texts under these headings
Should not have
• Old style
• Complex design

```html
<!DOCTYPE html>
<html lang="en">
<head>
<meta charset="utf-8">
<title>Kavak Verbatics – Translation, Localization &amp; Consultancy</title>
<link href="https://fonts.googleapis.com/css2?family=Roboto+Condensed:wght@300;400;700&family=Open+Sans:wght@300;400;600&display=swap" rel="stylesheet">
<style>
:root{
  --orange:#f7941d;
  --olive:#4a5a25;
  --olive-deep:#3f4d1f;
  --ink:#3a3a3a;
  --muted:#555;
  --white:#fff;
  --field-line:#fde3bd;
}
*{box-sizing:border-box;margin:0;padding:0}
html,body{width:1200px;height:3888px;overflow:hidden}
body{position:relative;background:var(--white);font-family:"Open Sans",Arial,sans-serif;color:var(--ink)}
h1,h2{font-weight:400}
.abs{position:absolute}
.center{left:0;width:1200px;text-align:center}
.heading{font-family:"Roboto Condensed","Arial Narrow",sans-serif;font-weight:400;font-size:44px;letter-spacing:.3px;text-transform:uppercase}
.heading .accent{color:var(--orange)}
.intro{font-size:14.5px;line-height:25px;color:var(--muted);text-align:center}

/* header */
.brand-mark{left:78px;top:24px;width:30px;height:30px;border-radius:50%;border:5px solid var(--orange)}
.brand-name{left:120px;top:16px;font-family:"Roboto Condensed",sans-serif;font-size:38px;line-height:42px;font-weight:400;color:var(--olive)}
.brand-tag{left:78px;top:66px;font-size:10px;font-weight:600;color:var(--olive);letter-spacing:.2px;text-transform:uppercase}
.header-phone{left:748px;top:18px;font-family:"Roboto Condensed",sans-serif;font-size:27px;font-weight:700;color:var(--orange);display:flex;align-items:center;gap:8px}
.btn-quote{left:964px;top:13px;width:156px;height:45px;background:var(--olive);color:var(--white);font-family:"Roboto Condensed",sans-serif;font-size:18px;line-height:45px;text-align:center;border-radius:3px}
.main-nav{left:376px;top:72px;width:745px;display:flex;justify-content:space-between;font-family:"Roboto Condensed",sans-serif;font-size:15px;color:var(--olive);text-transform:uppercase}
.main-nav .active{color:var(--orange)}

/* hero */
.hero{left:0;top:124px;width:1200px;height:576px;
  background:
    radial-gradient(ellipse 170px 210px at 82% 26%,rgba(214,160,96,.55),transparent 70%),
    radial-gradient(ellipse 300px 230px at 85% 72%,rgba(150,190,226,.85),transparent 72%),
    radial-gradient(ellipse 230px 170px at 42% 30%,rgba(120,128,140,.35),transparent 75%),
    radial-gradient(ellipse 260px 140px at 66% 86%,rgba(255,255,255,.9),transparent 75%),
    linear-gradient(100deg,#f3f4f3 0%,#e4e7e6 40%,#d6dadc 70%,#c9cfd3 100%)}
.hero-title{left:78px;top:296px;font-family:"Roboto Condensed",sans-serif;font-weight:400;font-size:53px;line-height:73px;color:var(--olive);text-transform:uppercase}
.btn-free{left:78px;top:459px;width:228px;height:46px;background:var(--orange);color:var(--white);border-radius:23px;font-family:"Roboto Condensed",sans-serif;font-size:19px;line-height:46px;text-align:center}

/* cards */
.card-photo{width:233px;height:135px}
.card-label{width:233px;text-align:center;font-family:"Roboto Condensed",sans-serif;font-size:20px;line-height:26px;text-transform:uppercase}
.card-label.orange{color:var(--orange)}
.card-text{width:233px;text-align:center;font-size:14px;line-height:25px;color:var(--muted)}

/* band */
.band{left:0;top:1221px;width:1200px;height:417px;
  background:
    radial-gradient(circle 230px at 24% 55%,rgba(214,222,226,.85),rgba(150,165,172,.4) 60%,transparent 80%),
    linear-gradient(90deg,#4d6572 0%,#6f8388 40%,#6c7d6a 75%,#55644f 100%)}
.band-text{left:500px;top:1322px;width:625px;text-align:right;font-family:"Open Sans",sans-serif;font-weight:300;font-size:35px;line-height:52px;color:var(--white)}

/* quote */
.quote-section{left:0;top:2053px;width:1200px;height:586px;background:var(--orange)}
.field{height:45px;border:2px solid var(--field-line);color:var(--white);font-size:15px;line-height:41px;padding-left:6px}
.field svg{position:absolute;right:12px;top:13px}
.btn-next{left:531px;top:2532px;width:135px;height:43px;border-radius:22px;background:var(--olive);color:var(--white);font-family:"Roboto Condensed",sans-serif;font-size:18px;line-height:43px;text-align:center}
.step{left:480px;top:2208px;display:flex;align-items:center;gap:12px;color:var(--white);font-family:"Roboto Condensed",sans-serif;font-size:21px}

/* testimonial */
.testimonial{left:0;top:2639px;width:1200px;height:355px;
  background:
    radial-gradient(ellipse 260px 200px at 18% 70%,rgba(150,160,120,.45),transparent 75%),
    radial-gradient(ellipse 300px 220px at 86% 60%,rgba(170,176,140,.4),transparent 75%),
    linear-gradient(90deg,#4d5d33 0%,#66764a 50%,#4a5a2f 100%)}
.testimonial-text{left:200px;top:2816px;width:800px;color:var(--white);font-size:14px;line-height:24px;text-align:center}
.client{color:var(--orange);font-size:12px;font-weight:600;letter-spacing:.5px}

/* team */
.portrait{width:150px;height:150px;border-radius:50%;border:5px solid var(--orange);
  background:linear-gradient(180deg,#eef0f2 0%,#d9c6b2 45%,#6f7782 100%)}

/* banner */
.banner{left:0;top:3491px;width:1200px;height:148px;background:var(--orange)}
.banner-text{top:3545px;color:var(--white);font-family:"Roboto Condensed",sans-serif;font-size:42px;letter-spacing:.5px;text-transform:uppercase}

/* footer */
.footer{left:0;top:3639px;width:1200px;height:249px;background:var(--olive-deep)}
.footer-nav{left:80px;top:3667px;display:flex;gap:26px;color:var(--white);font-size:16px}
.social{left:934px;top:3667px;display:flex;gap:40px}
.social span{width:16px;height:16px;border-radius:50%;background:var(--white);display:block}
.social span.first{background:var(--orange)}
.contact-title{left:80px;top:3732px;color:var(--orange);font-size:21px}
.contact-item{display:flex;align-items:center;gap:12px;color:var(--white);font-size:13px;line-height:19px}
.icon-dot{width:36px;height:36px;border-radius:50%;background:var(--white);display:flex;align-items:center;justify-content:center;flex:none}
.copyright{top:3838px;color:var(--white);font-size:13px}
.copyright b{color:var(--orange);font-weight:600}
</style>
</head>
<body>

<!-- header -->
<div class="abs brand-mark"></div>
<div class="abs brand-name">Kavak Verbatics</div>
<div class="abs brand-tag">Translation, Localization &amp; Consultancy</div>
<div class="abs header-phone">
  <svg width="22" height="22" viewBox="0 0 24 24"><path fill="#f7941d" d="M6.6 10.8a15.1 15.1 0 0 0 6.6 6.6l2.2-2.2c.3-.3.7-.4 1-.2 1.1.4 2.3.6 3.6.6.6 0 1 .4 1 1V20c0 .6-.4 1-1 1A17 17 0 0 1 3 4c0-.6.4-1 1-1h3.5c.6 0 1 .4 1 1 0 1.3.2 2.5.6 3.6.1.3 0 .7-.2 1z"/></svg>
  0 212 555 0148
</div>
<div class="abs btn-quote">GET A QUOTE</div>
<nav class="abs main-nav">
  <span class="active">Home</span><span>Translation Services</span><span>Languages</span><span>Resources</span><span>Pricing</span><span>About</span><span>Blog</span><span>Contact</span>
</nav>

<!-- hero -->
<div class="abs hero" role="img" aria-label="Photo of a smiling translator in a light blue shirt working at a laptop in a bright office with colleagues behind her"></div>
<h1 class="abs hero-title">Delivery on time with<br>perfect quality</h1>
<div class="abs btn-free">GET A FREE QUOTE</div>

<!-- welcome -->
<h2 class="abs center heading" style="top:748px"><span class="accent">Welcome to</span> Kavak Verbatics</h2>
<p class="abs intro" style="left:181px;top:812px;width:838px">Lorem Ipsum is simply dummy text of the printing and typesetting industry. Lorem Ipsum has been the industry's standard dummy text ever since the 1500s, when an unknown printer took a galley of type and scrambled it to make a type specimen book.</p>

<div class="abs card-photo" style="left:78px;top:915px;background:linear-gradient(120deg,#23272d 0%,#5b6068 30%,#e6e3df 52%,#3a3e45 72%,#16191e 100%)" role="img" aria-label="Photo of business people in suits in a meeting"></div>
<div class="abs card-photo" style="left:350px;top:915px;background:linear-gradient(160deg,#f5f5f4 0%,#dcdcdb 40%,#c7a58a 62%,#8e9298 100%)" role="img" aria-label="Photo of hands typing on a laptop"></div>
<div class="abs card-photo" style="left:619px;top:915px;background:radial-gradient(ellipse 90px 55px at 50% 52%,#e8e4dc,#8a8680 60%,#1e2530 100%)" role="img" aria-label="Photo of a team around a table seen from above"></div>
<div class="abs card-photo" style="left:889px;top:915px;background:radial-gradient(ellipse 120px 80px at 55% 45%,#bfe3f7,#4b95cf 55%,#17497f 100%)" role="img" aria-label="Photo of a businessman with a digital interface"></div>

<div class="abs card-label orange" style="left:78px;top:1063px">Translation</div>
<div class="abs card-label" style="left:350px;top:1063px">Interpretation</div>
<div class="abs card-label orange" style="left:619px;top:1063px">Localization &amp;<br>Consultancy</div>
<div class="abs card-label orange" style="left:889px;top:1063px">Translation API</div>

<p class="abs card-text" style="left:78px;top:1094px">Lorem Ipsum is simply dummy text of the printing and typesetting industry.</p>
<p class="abs card-text" style="left:350px;top:1094px">Lorem Ipsum is simply dummy text of the printing and typesetting industry.</p>
<p class="abs card-text" style="left:619px;top:1125px">Lorem Ipsum is simply dummy text of the printing.</p>
<p class="abs card-text" style="left:889px;top:1094px">Lorem Ipsum is simply dummy text of the printing and typesetting industry.</p>

<!-- band -->
<div class="abs band" role="img" aria-label="Image of a silver wireframe globe over a blue-green technology backdrop"></div>
<p class="abs band-text">Lorem Ipsum is simply dummy text of the printing and typesetting industry. Lorem Ipsum has been the industry's standard dummy text.</p>

<!-- translation services -->
<h2 class="abs center heading" style="top:1689px"><span class="accent">Translation</span> Services</h2>

<div class="abs card-photo" style="left:78px;top:1760px;background:linear-gradient(110deg,#f0ede8 0%,#c9b9a6 30%,#2c3038 55%,#e7e7e6 78%,#9aa0a8 100%)" role="img" aria-label="Photo of a marketing team meeting"></div>
<div class="abs card-photo" style="left:350px;top:1760px;background:radial-gradient(ellipse 80px 45px at 48% 45%,#7a4a2a,#a77a58 45%,#eeeeed 80%)" role="img" aria-label="Photo of a judge's gavel"></div>
<div class="abs card-photo" style="left:619px;top:1760px;background:radial-gradient(ellipse 110px 80px at 55% 60%,#c8e2f6,#3f7dc0 55%,#12305e 100%)" role="img" aria-label="Photo of a hand touching a technical interface"></div>
<div class="abs card-photo" style="left:889px;top:1760px;background:linear-gradient(130deg,#ece8e2 0%,#cdbfae 40%,#4a4f57 62%,#d9d6d1 100%)" role="img" aria-label="Photo of people signing documents"></div>

<div class="abs card-label orange" style="left:78px;top:1908px;font-size:17.5px">Marketing Translation</div>
<div class="abs card-label" style="left:350px;top:1908px;font-size:17.5px">Legal Translation</div>
<div class="abs card-label orange" style="left:619px;top:1908px;font-size:17.5px">Technical Translation</div>
<div class="abs card-label orange" style="left:889px;top:1908px;font-size:17.5px">Personal Translation</div>

<p class="abs card-text" style="left:78px;top:1942px">Lorem Ipsum is simply dummy text of the printing and typesetting industry.</p>
<p class="abs card-text" style="left:350px;top:1942px">Lorem Ipsum is simply dummy text of the printing and typesetting industry.</p>
<p class="abs card-text" style="left:619px;top:1942px">Lorem Ipsum is simply dummy text of the printing and typesetting industry.</p>
<p class="abs card-text" style="left:889px;top:1942px">Lorem Ipsum is simply dummy text of the printing and typesetting industry.</p>

<!-- quote form -->
<section class="abs quote-section"></section>
<h2 class="abs center heading" style="top:2105px;color:#fff">Translation Quote</h2>
<p class="abs center intro" style="top:2164px;color:#fff">Lorem ipsum is simply dummy text of the printing and typesetting industry.</p>
<div class="abs step">
  <svg width="56" height="56" viewBox="0 0 56 56">
    <circle cx="28" cy="28" r="22" fill="none" stroke="#fff" stroke-width="3" stroke-dasharray="3 6"/>
    <text x="28" y="35" text-anchor="middle" fill="#fff" font-family="Roboto Condensed,sans-serif" font-size="20">1</text>
  </svg>
  Time &amp; Languages
</div>
<div class="abs field" style="left:277px;top:2284px;width:311px">Timeframe<svg width="18" height="14" viewBox="0 0 18 14"><path d="M2 3l7 7 7-7" fill="none" stroke="#fff" stroke-width="2.5"/></svg></div>
<div class="abs field" style="left:612px;top:2284px;width:308px">Certification<svg width="18" height="14" viewBox="0 0 18 14"><path d="M2 3l7 7 7-7" fill="none" stroke="#fff" stroke-width="2.5"/></svg></div>
<div class="abs field" style="left:277px;top:2351px;width:311px">Source Language</div>
<div class="abs field" style="left:612px;top:2351px;width:308px">Target Language</div>
<div class="abs field" style="left:277px;top:2416px;width:643px;height:93px">Note</div>
<div class="abs btn-next">NEXT</div>

<!-- testimonial -->
<section class="abs testimonial" role="img" aria-label="Photo of two colleagues talking in an office, tinted green"></section>
<h2 class="abs center heading" style="top:2688px;color:#fff">What Our Client Say</h2>
<svg class="abs" style="left:579px;top:2766px" width="42" height="34" viewBox="0 0 42 34"><path fill="#f7941d" d="M2 34V20C2 9 7 3 17 0l2 4c-6 2-8 6-8 11h8v19zM24 34V20c0-11 5-17 15-20l2 4c-6 2-8 6-8 11h8v19z"/></svg>
<p class="abs testimonial-text">Lorem Ipsum is simply dummy text of the printing and typesetting industry. Lorem Ipsum has been the industry's standard dummy text ever since the 1500s, when an unknown printer took a galley of type and scrambled it to make a type specimen book.<br><span class="client">- CLIENT NAME</span></p>

<!-- team -->
<h2 class="abs center heading" style="top:3039px"><span class="accent">Meet Our</span> Dedicated Team</h2>
<p class="abs intro" style="left:260px;top:3104px;width:680px">Lorem Ipsum is simply dummy text of the printing and typesetting industry. Lorem Ipsum has been the industry's standard dummy text ever since the 1500.</p>

<div class="abs portrait" style="left:119px;top:3179px" role="img" aria-label="Portrait photo of a team member"></div>
<div class="abs portrait" style="left:389px;top:3179px" role="img" aria-label="Portrait photo of a team member"></div>
<div class="abs portrait" style="left:661px;top:3179px" role="img" aria-label="Portrait photo of a team member"></div>
<div class="abs portrait" style="left:930px;top:3179px" role="img" aria-label="Portrait photo of a team member"></div>

<div class="abs card-label orange" style="left:78px;top:3344px;font-size:17.5px">Team Name</div>
<div class="abs card-label orange" style="left:350px;top:3344px;font-size:17.5px">Team Name</div>
<div class="abs card-label orange" style="left:619px;top:3344px;font-size:17.5px">Team Name</div>
<div class="abs card-label orange" style="left:889px;top:3344px;font-size:17.5px">Team Name</div>

<p class="abs card-text" style="left:78px;top:3371px">Lorem Ipsum is simply dummy text of the printing and typesetting industry.</p>
<p class="abs card-text" style="left:350px;top:3371px">Lorem Ipsum is simply dummy text of the printing and typesetting industry.</p>
<p class="abs card-text" style="left:619px;top:3371px">Lorem Ipsum is simply dummy text of the printing and typesetting industry.</p>
<p class="abs card-text" style="left:889px;top:3371px">Lorem Ipsum is simply dummy text of the printing and typesetting industry.</p>

<!-- banner -->
<section class="abs banner"></section>
<svg class="abs" style="left:568px;top:3491px" width="64" height="28" viewBox="0 0 64 28"><path d="M0 0h64L32 28z" fill="#fff"/></svg>
<p class="abs center banner-text">Lorem Ipsum is simply dummy text.</p>

<!-- footer -->
<footer class="abs footer"></footer>
<nav class="abs footer-nav"><span>Home</span><span>About</span><span>Contact Us</span><span>Job Vacancies</span><span>Privacy Policy</span></nav>
<div class="abs social"><span class="first"></span><span></span><span></span><span></span></div>
<div class="abs contact-title">Contact Us</div>

<div class="abs contact-item" style="left:80px;top:3772px;width:250px">
  <span class="icon-dot" style="background:var(--orange)"><svg width="16" height="20" viewBox="0 0 16 20"><path fill="#fff" d="M8 0a7 7 0 0 0-7 7c0 5 7 13 7 13s7-8 7-13a7 7 0 0 0-7-7zm0 10a3 3 0 1 1 0-6 3 3 0 0 1 0 6z"/></svg></span>
  <span>Ilgın Sok. Peker Apt. No. 12 Daire 3 Çamlıtepe, 34410</span>
</div>
<div class="abs contact-item" style="left:350px;top:3780px">
  <span class="icon-dot"><svg width="12" height="18" viewBox="0 0 12 18"><rect x="1" y="1" width="10" height="16" rx="2" fill="none" stroke="#3f4d1f" stroke-width="2"/></svg></span>
  <span>0 212 555 0148</span>
</div>
<div class="abs contact-item" style="left:622px;top:3780px">
  <span class="icon-dot"><svg width="18" height="16" viewBox="0 0 18 16"><rect x="1" y="5" width="16" height="8" rx="1" fill="#3f4d1f"/><rect x="4" y="1" width="10" height="5" fill="none" stroke="#3f4d1f" stroke-width="1.6"/><rect x="4" y="10" width="10" height="5" fill="#fff" stroke="#3f4d1f" stroke-width="1.6"/></svg></span>
  <span>0 532 555 0193</span>
</div>
<div class="abs contact-item" style="left:890px;top:3780px">
  <span class="icon-dot"><svg width="18" height="14" viewBox="0 0 18 14"><rect x="1" y="1" width="16" height="12" rx="1" fill="none" stroke="#3f4d1f" stroke-width="1.8"/><path d="M1 2l8 6 8-6" fill="none" stroke="#3f4d1f" stroke-width="1.8"/></svg></span>
  <span>info@kvkaktarim.example</span>
</div>
<p class="abs center copyright">© 2016 <b>KAVAK VERBATICS</b>. All Rights Reserved.</p>

</body>
</html>
```